Clinic Harbor brouchure

I am attaching a sample of what I would like to be created in a vector format or format that I can send to a printer.

The Clinic Harbor logo is the style I like.

Thanks, Alan
Updates

Project Deadline Extended Reason: I have extended the deadline. Thanks for your understanding.Sincerely, Alan Added Friday, March 24, 2017

Industry/Entity Type

Printer

Font styles to use
Other font styles liked:
• please see attached

Requirements
Must have
• please create a format that I can provide to a printer for making a brochure
• UPDATE: please if possible, have the size be 10'' wide by 11'' tall
• with the brochure opening from top to bottom like a calendar
Nice to have
• I like where you are going with this, can you put an image on the top of the page and the text on the bottom of the page
• when you are holding the marketing piece, it should be 10'' wide by 5.5'' tall, after you open the cover page, then it becomes 10'' wide by 11'' tall
• the top page is an image and the lower page is the message..
• so when you view it you see a picture and then text
• the front cover should have the logo image -
• Clinic Harbor
• the wording - cost effective resources for your practice
• cash back medical plans, 15% medical wellness discount
• on the inside pages 1-3 keep the tag line Clinic Harbor / Practice Management
• the contact info on page 4
• the last page - Clinic Harbor logo in the middle, then Practice Management on the bottom

```html
<!DOCTYPE html>
<html lang="en">
<head>
<meta charset="utf-8">
<title>Clinic Harbor Brochure</title>
<link href="https://fonts.googleapis.com/css2?family=Roboto+Condensed:ital,wght@0,400;0,700;1,400&display=swap" rel="stylesheet">
<style>
:root{
  --navy:#1c3a8c;
  --blue:#1473d6;
  --sky:#27a9ee;
  --ink:#222;
  --grey:#b8bcc4;
  --paper:#f4f5f7;
  --stage:#ececec;
}
*{box-sizing:border-box;margin:0;padding:0}
html,body{width:1200px;height:995px;overflow:hidden}
body{
  background:radial-gradient(ellipse at center,#fafafa 0%,var(--stage) 100%);
  font-family:"Roboto Condensed",sans-serif;
  position:relative;
}
.page{
  position:absolute;width:362px;height:397px;
  background:linear-gradient(180deg,#fff 0%,var(--paper) 100%);
  box-shadow:0 1px 4px rgba(0,0,0,.25);
  overflow:hidden;
}
.page--front{left:30px;top:28px}
.page--two{left:422px;top:28px}
.page--three{left:812px;top:28px}
.page--four{left:218px;top:516px}
.page--back{left:615px;top:516px}

.page__header{position:absolute;left:0;top:0;width:100%;height:16px;z-index:3}
.page__footer{position:absolute;left:0;bottom:0;width:100%;height:27px;background:#fff;z-index:3}
.page__url{position:absolute;left:0;top:3px;width:100%;text-align:center;font-size:9px;color:var(--ink)}
.page__footbar{position:absolute;left:0;bottom:0;width:100%;height:8px;background:var(--blue)}
.page__footbar::after{content:"";position:absolute;right:10px;top:0;width:8px;height:8px;background:var(--navy)}

.brand{
  position:absolute;left:0;top:28px;width:100%;height:44px;z-index:2;
  display:flex;justify-content:center;align-items:center;gap:8px;
}
.brand__mark{width:12px;height:12px;border-radius:50%;background:var(--navy)}
.brand__name{font-weight:700;font-size:28px;color:var(--navy);letter-spacing:.3px}
.brand__tag{font-size:11px;font-style:italic;color:#555;line-height:1.3;border-left:1px solid #999;padding-left:6px;margin-left:2px}

.visual{position:absolute;left:0;width:100%}
.visual--front{
  top:16px;height:274px;
  background:
    radial-gradient(ellipse 45% 55% at 22% 55%,rgba(255,255,255,.95) 0%,rgba(255,255,255,0) 70%),
    radial-gradient(circle at 42% 38%,rgba(40,90,170,.45) 0 7%,rgba(40,90,170,0) 10%),
    radial-gradient(circle at 62% 38%,rgba(60,110,190,.35) 0 7%,rgba(60,110,190,0) 10%),
    radial-gradient(circle at 84% 38%,rgba(60,110,190,.35) 0 7%,rgba(60,110,190,0) 10%),
    radial-gradient(ellipse 30% 20% at 80% 70%,rgba(40,100,190,.35) 0%,rgba(40,100,190,0) 80%),
    linear-gradient(135deg,#dce9f6 0%,#b8d3ef 45%,#e9f1fa 100%);
}
.visual--steth{
  top:16px;height:354px;
  background:
    radial-gradient(ellipse 38% 22% at 48% 66%,#101418 0 55%,rgba(16,20,24,0) 75%),
    radial-gradient(ellipse 60% 30% at 60% 45%,rgba(110,190,210,.55) 0%,rgba(110,190,210,0) 70%),
    linear-gradient(150deg,#0a2232 0%,#1b5a72 40%,#2f7f98 55%,#0d3347 75%,#061722 100%);
}
.visual--runner{
  top:16px;height:354px;
  background:
    radial-gradient(ellipse 28% 45% at 50% 48%,rgba(180,225,255,.7) 0%,rgba(180,225,255,0) 75%),
    linear-gradient(180deg,rgba(255,255,255,0) 48%,rgba(170,225,255,.55) 50%,rgba(255,255,255,0) 52%),
    linear-gradient(160deg,#0f4aa8 0%,#1d6ad0 45%,#1460c4 70%,#0d3f9e 100%);
}
.visual--desk{
  top:142px;height:144px;
  background:
    radial-gradient(ellipse 20% 25% at 42% 55%,rgba(120,130,140,.5) 0%,rgba(120,130,140,0) 80%),
    linear-gradient(165deg,rgba(255,255,255,0) 40%,rgba(30,90,110,.35) 48%,rgba(255,255,255,0) 56%),
    linear-gradient(160deg,#f4f6f8 0%,#dde3e9 55%,#eef1f4 100%);
}

.band{position:absolute;left:0;width:100%;background:var(--navy);color:#fff;text-transform:uppercase;z-index:1}
.band--front{top:290px;height:80px;padding:5px 0 0 17px}
.band__lead{font-size:21px;color:var(--sky);letter-spacing:.2px}
.band__title{font-size:29px;line-height:1.15;letter-spacing:.5px}
.band__perks{display:flex;gap:14px;margin-top:4px;font-size:8px;align-items:center}
.band__perk{display:flex;align-items:center;gap:4px}

.band--intro{top:117px;height:53px;padding:5px 0 0 17px}
.band--intro .band__lead{font-size:19.5px;line-height:1.15;letter-spacing:.6px}
.band__sub{font-size:19.5px;line-height:1.15;letter-spacing:.3px}
.page__body{
  position:absolute;left:17px;right:18px;top:228px;
  font-size:10.5px;line-height:1.35;letter-spacing:.55px;color:var(--blue);text-transform:uppercase;text-align:justify;
}
.band--access{top:316px;height:54px;padding:6px 18px 0 17px;font-size:9.6px;line-height:1.4;letter-spacing:.3px;text-align:center}

.band--relation{top:86px;height:56px;padding:7px 84px 0 17px;font-size:12px;line-height:1.3;letter-spacing:.2px}
.band--services{top:286px;height:37px;padding:5px 10px 0;font-size:10px;text-align:center;line-height:1.3}

.contact{position:absolute;left:0;top:332px;width:100%;text-align:center}
.contact__cta{display:flex;justify-content:center;align-items:center;gap:4px;font-weight:700;font-size:13px;color:var(--ink)}
.contact__phone{display:inline-block;margin-top:3px;background:var(--navy);color:#fff;font-size:13px;padding:0 7px;border-radius:2px;line-height:16px}

.tiles{position:absolute;z-index:2}
.label{position:absolute;font-size:22px;color:#333;letter-spacing:.5px;text-align:center;width:362px}
</style>
</head>
<body>

<svg width="0" height="0" style="position:absolute">
  <defs>
    <g id="header-strip">
      <rect x="0" y="0" width="362" height="5" fill="#1473d6"/>
      <polygon points="0,5 285,5 275,11 0,11" fill="#ffffff"/>
      <polygon points="275,11 285,5 362,5 362,14 270,14" fill="#1473d6"/>
      <rect x="0" y="11" width="272" height="3" fill="#e6e9ee"/>
      <rect x="0" y="14" width="362" height="2" fill="#1c3a8c" opacity=".85"/>
    </g>
    <g id="tile-cluster">
      <rect x="32" y="0" width="32" height="28" fill="#27a9ee"/>
      <rect x="8" y="8" width="14" height="14" fill="#b8bcc4"/>
      <rect x="24" y="22" width="18" height="18" fill="#1c3a8c"/>
      <rect x="44" y="30" width="20" height="20" fill="#1c3a8c" opacity=".9"/>
      <rect x="14" y="34" width="26" height="24" fill="#27a9ee"/>
      <rect x="0" y="30" width="9" height="9" fill="#ffffff"/>
    </g>
  </defs>
</svg>

<!-- FRONT PAGE -->
<section class="page page--front">
  <svg class="page__header" viewBox="0 0 362 16"><use href="#header-strip"/></svg>
  <div class="visual visual--front" role="img" aria-label="Gloved hand touching floating medical icons, stethoscope and world map"></div>
  <div class="brand"><span class="brand__mark"></span><span class="brand__name">Clinic Harbor</span></div>
  <svg class="tiles" style="left:298px;top:258px" width="64" height="62" viewBox="0 0 64 62"><use href="#tile-cluster"/></svg>
  <div class="band band--front">
    <div class="band__lead">Cost Effective Resources</div>
    <div class="band__title">For Your Practice</div>
    <div class="band__perks">
      <span class="band__perk"><svg width="12" height="12" viewBox="0 0 12 12"><circle cx="6" cy="6" r="5" fill="none" stroke="#fff" stroke-width="1.4"/><text x="6" y="9" font-size="8" text-anchor="middle" fill="#fff" font-family="sans-serif">$</text></svg>Cash Back Medical Plans</span>
      <span class="band__perk"><svg width="12" height="12" viewBox="0 0 12 12"><path d="M6 10.5 1.5 6A2.6 2.6 0 0 1 6 2.8 2.6 2.6 0 0 1 10.5 6Z" fill="none" stroke="#fff" stroke-width="1.4"/></svg>15% Wellness Medical Discount</span>
    </div>
  </div>
  <div class="page__footer"><div class="page__url">www.clinicharbor.com</div><div class="page__footbar"></div></div>
</section>

<!-- PAGE 2 -->
<section class="page page--two">
  <svg class="page__header" viewBox="0 0 362 16"><use href="#header-strip"/></svg>
  <div class="visual visual--steth" role="img" aria-label="Close-up of a stethoscope chest piece on a dark teal background"></div>
  <div class="page__footer"><div class="page__url">www.clinicharbor.com</div><div class="page__footbar"></div></div>
</section>

<!-- PAGE 3 -->
<section class="page page--three">
  <svg class="page__header" viewBox="0 0 362 16"><use href="#header-strip"/></svg>
  <div class="brand"><span class="brand__mark"></span><span class="brand__name">Clinic Harbor</span><span class="brand__tag">Practice<br>Management</span></div>
  <svg class="tiles" style="left:298px;top:80px" width="64" height="62" viewBox="0 0 64 62"><use href="#tile-cluster"/></svg>
  <div class="band band--intro">
    <div class="band__lead">With Clinic Harbor,</div>
    <div class="band__sub">Your Practice Comes First.</div>
  </div>
  <p class="page__body">The Clinic Harbor Practice Management Program is expressly designed to enhance your practice. From cash back on select medical plans to low cost practice payroll fees.</p>
  <div class="band band--access">With Clinic Harbor your practice will have access to products and services that help put thousands of dollars back into your practice each year.</div>
  <div class="page__footer"><div class="page__url">www.clinicharbor.com</div><div class="page__footbar"></div></div>
</section>

<!-- PAGE 4 -->
<section class="page page--four">
  <svg class="page__header" viewBox="0 0 362 16"><use href="#header-strip"/></svg>
  <div class="visual visual--runner" role="img" aria-label="Glowing blue x-ray figure running beside a heartbeat line"></div>
  <div class="page__footer"><div class="page__url">www.clinicharbor.com</div><div class="page__footbar"></div></div>
</section>

<!-- BACK PAGE -->
<section class="page page--back">
  <svg class="page__header" viewBox="0 0 362 16"><use href="#header-strip"/></svg>
  <div class="brand"><span class="brand__mark"></span><span class="brand__name">Clinic Harbor</span></div>
  <svg class="tiles" style="left:298px;top:48px" width="64" height="62" viewBox="0 0 64 62"><use href="#tile-cluster"/></svg>
  <div class="band band--relation">Clinic Harbor Practice Management is a relationship that gives your practice time, cost and rewards.</div>
  <div class="visual visual--desk" role="img" aria-label="Stethoscope and pen resting on a medical chart"></div>
  <div class="band band--services">Proven guidance in group benefits, payroll, human resources,<br>workers compensation, 401(k) and more</div>
  <div class="contact">
    <div class="contact__cta"><svg width="13" height="13" viewBox="0 0 24 24"><path d="M6.6 10.8a15 15 0 0 0 6.6 6.6l2.2-2.2a1 1 0 0 1 1-.25 11.4 11.4 0 0 0 3.6.57 1 1 0 0 1 1 1V20a1 1 0 0 1-1 1A17 17 0 0 1 3 4a1 1 0 0 1 1-1h3.5a1 1 0 0 1 1 1 11.4 11.4 0 0 0 .57 3.6 1 1 0 0 1-.25 1Z" fill="#222"/></svg>CALL US NOW!</div>
    <div class="contact__phone">407-555-0186</div>
  </div>
  <div class="page__footer"><div class="page__url">www.clinicharbor.com</div><div class="page__footbar"></div></div>
</section>

<div class="label" style="left:30px;top:446px">FRONT PAGE</div>
<div class="label" style="left:422px;top:446px">PAGE 2</div>
<div class="label" style="left:812px;top:446px">PAGE 3</div>
<div class="label" style="left:218px;top:934px">PAGE 4</div>
<div class="label" style="left:615px;top:934px">BACK PAGE</div>

</body>
</html>
```